UPDATE: I have uploaded the selected logo from the other contest, please use it in your designs.

I have a logo design contest as well so not sure how ArtHive handles that. They should integrate at some point. I will describe the overall theme with the logo description. See it for details.

The business card side of it would just build on that same theme.

Target Market(s)

8-40

Industry/Entity Type

Business

Contact Information for Business Card

FirstName LastName
Email

Logo Text

VelMarin

Font styles to use
Sans Serif

Requirements
Must have
• the url VelMarin.com somewhere in it.

```html
<!DOCTYPE html>
<html lang="en">
<head>
<meta charset="utf-8">
<title>VelMarin Business Card</title>
<link href="https://fonts.googleapis.com/css2?family=Audiowide&display=swap" rel="stylesheet">
<style>
  :root {
    --backdrop: #a6a6a6;
    --card-white: #ffffff;
    --brand-blue: #1d73be;
    --brand-green: #8cc63f;
    --panel-dark: #2a2b2d;
    --panel-darker: #1c1d1f;
    --text-light: #f4f4f4;
  }
  * { margin: 0; padding: 0; box-sizing: border-box; }
  html, body {
    width: 1200px;
    height: 900px;
    overflow: hidden;
    background: var(--backdrop);
  }
  .canvas {
    width: 1200px;
    height: 900px;
    display: flex;
    align-items: center;
    justify-content: center;
  }
  .card {
    position: relative;
    width: 880px;
    height: 530px;
    border-radius: 44px;
    overflow: hidden;
    background: var(--card-white);
    font-family: "Audiowide", sans-serif;
  }
  .card-top {
    position: absolute;
    inset: 0 0 auto 0;
    height: 270px;
    display: flex;
    align-items: center;
    justify-content: center;
  }
  .brand-name {
    font-size: 86px;
    letter-spacing: 6px;
    color: var(--brand-blue);
    text-transform: uppercase;
    font-weight: 400;
  }
  .accent-band {
    position: absolute;
    left: 0;
    right: 0;
    top: 270px;
    height: 16px;
    background: var(--brand-blue);
  }
  .card-bottom {
    position: absolute;
    left: 0;
    right: 0;
    top: 286px;
    bottom: 0;
    background: linear-gradient(180deg, var(--panel-dark), var(--panel-darker));
    display: flex;
    flex-direction: column;
    align-items: center;
    justify-content: center;
    gap: 6px;
  }
  .person-name {
    font-size: 50px;
    color: var(--brand-green);
    text-transform: uppercase;
    letter-spacing: 2px;
    margin-bottom: 18px;
    font-weight: 400;
  }
  .contact-line {
    font-size: 31px;
    color: var(--text-light);
    text-transform: uppercase;
    letter-spacing: 1px;
    line-height: 1.15;
  }
</style>
</head>
<body>
  <main class="canvas">
    <article class="card">
      <header class="card-top">
        <h1 class="brand-name">VelMarin</h1>
      </header>
      <div class="accent-band"></div>
      <section class="card-bottom" role="img" aria-label="Dark perforated dot-texture panel holding the contact details">
        <h2 class="person-name">Lena Hart</h2>
        <p class="contact-line">info@velmarin.com</p>
        <p class="contact-line">www.velmarin.com</p>
      </section>
    </article>
  </main>
</body>
</html>
```